Webdesign für K&L Vendora GmbH
Zielgruppe
- Partner für moderne Automaten- und Verpflegungslösungen in Unternehmen
- Zielgruppe sind Unternehmen, welche Versorgungskonzepte schaffen, die optimal auf die Bedürfnisse von Mitarbeitenden, Kunden und Gästen abgestimmt sind
Aufgabenstellung
- KEINE Kopie der alten Webseite
- Farbkonzept gern in sanften Kaffeetönen kombiniert mit Weiß
- Klare Struktur der Webseite

```html
<!DOCTYPE html>
<html lang="de">
<head>
<meta charset="utf-8">
<title>K&amp;L Vendora GmbH – Automaten für Büro und Betrieb</title>
<link rel="stylesheet" href="https://fonts.googleapis.com/css2?family=Roboto:wght@400;500;700;900&family=Roboto+Condensed:wght@400;500;700&display=swap">
<style>
:root{
  --red:#a51c30;
  --red-deep:#6e1420;
  --ink:#0f0d0c;
  --white:#ffffff;
  --muted:#d9d4cf;
  --line:rgba(255,255,255,.35);
  --band:rgba(120,112,106,.45);
  --sans:"Roboto",Arial,sans-serif;
  --cond:"Roboto Condensed","Arial Narrow",sans-serif;
}
*{margin:0;padding:0;box-sizing:border-box}
html,body{width:1200px;height:2400px;overflow:hidden;background:#fff}
body{position:relative;font-family:var(--sans);color:var(--white)}
.page{position:absolute;left:160px;top:88px;width:887px;height:2238px;overflow:hidden;background:var(--ink)}
.abs{position:absolute}
.scene{position:absolute;inset:0;
  background:
   radial-gradient(ellipse 260px 420px at 760px 1500px,rgba(150,100,45,.55),transparent 70%),
   radial-gradient(ellipse 240px 260px at 140px 700px,rgba(120,80,40,.5),transparent 70%),
   radial-gradient(ellipse 300px 200px at 700px 1080px,rgba(110,75,40,.45),transparent 70%),
   radial-gradient(ellipse 420px 260px at 420px 760px,rgba(90,80,72,.45),transparent 70%),
   linear-gradient(180deg,#1a1614 0%,#231d19 30%,#1a1512 55%,#120f0d 80%,#0e0c0b 100%)}
.machines{position:absolute;left:500px;top:85px;width:320px;height:305px;
  background:radial-gradient(ellipse 70px 130px at 250px 150px,rgba(200,120,40,.55),transparent 75%),
   radial-gradient(ellipse 70px 110px at 95px 140px,rgba(190,130,60,.45),transparent 75%),
   linear-gradient(90deg,#171413,#201a16 50%,#16120f)}
/* header */
.logo{left:62px;top:24px;font:900 20px/1 var(--sans);letter-spacing:.5px}
.nav a{position:absolute;top:34px;font:500 12.5px/1 var(--cond);color:var(--white);text-decoration:none}
.nav .active{left:371px;top:26px;width:80px;height:26px;background:var(--white);color:var(--red);border-radius:4px 4px 0 0;padding:8px 0 0 5px;font-weight:700}
.nav .meta{font:400 9.5px/1 var(--sans);top:36px}
.rule{left:62px;width:762px;height:1px;background:var(--line)}
.dropdown{left:371px;top:52px;width:129px;height:125px;background:var(--white);border-radius:0 4px 4px 4px;z-index:3;list-style:none;padding:8px 0 0 10px}
.dropdown li{font:400 10.5px/21.6px var(--sans);color:#333}
.dropdown li.current{color:var(--red)}
/* hero */
.headline{left:62px;top:110px;font:700 68px/66px var(--sans);letter-spacing:-.5px;z-index:2}
.headline em{font-style:normal;color:var(--red)}
.subline{left:62px;top:318px;font:400 24px/22px var(--cond)}
.btn{top:388px;height:30px;border-radius:4px;font:500 10.5px/30px var(--sans);text-align:center}
.btn-primary{left:62px;width:135px;background:var(--red)}
.btn-outline{left:218px;width:105px;border:1px solid var(--red)}
.features{left:62px;top:459px;width:762px;height:84px;background:var(--band);border-radius:4px}
.feature{top:474px;width:131px;height:55px;background:var(--red);border-radius:3px;display:flex;align-items:center;gap:6px;padding:0 10px;font:500 11px/12px var(--sans)}
.feature svg{flex:none}
/* sections */
.section-title{left:0;width:887px;text-align:center;font:500 24px/1 var(--cond)}
.timeline{left:442px;top:660px;width:1.5px;height:388px;background:var(--white)}
.dot{width:15px;height:15px;border-radius:50%;background:var(--white);left:435px}
.step{font-family:var(--cond)}
.step h3{font:500 13.5px/1 var(--cond);margin-bottom:6px}
.step p{font:400 10.5px/12.5px var(--cond);text-transform:uppercase}
.step.left{text-align:right;right:459px}
.step.right{left:457px}
.photo-round{width:86px;height:86px;border-radius:50%;border:2px solid rgba(255,255,255,.5)}
/* products */
.card{width:220px;height:264px;border-radius:8px;overflow:hidden;border:1px solid rgba(0,0,0,.4)}
.card .cap{position:absolute;left:10px;bottom:12px}
.card h4{font:500 13.5px/1 var(--sans);margin-bottom:4px}
.card p{font:400 10.5px/11.5px var(--sans)}
.arrow{width:28px;height:28px;border-radius:50%;background:var(--white);top:1626px}
/* contact */
.contact-lead{left:62px;top:1772px;font:500 13.5px/1 var(--cond)}
.contact-text{left:62px;font:400 10.5px/12.5px var(--sans);width:270px}
.contact-row{left:62px;display:flex;gap:6px;font:400 10.5px/12.5px var(--sans)}
.map{left:516px;top:1772px;width:308px;height:280px;border-radius:8px;
  background:linear-gradient(135deg,#eef0f2,#e3e6ea 60%,#dfe3e8)}
/* footer */
.foot-col{top:2103px;font:400 8.5px/18.5px var(--sans);color:var(--muted)}
.foot-col h5{font:500 11px/1 var(--sans);color:var(--white);margin-bottom:8px}
.foot-about{line-height:9.5px;width:120px}
</style>
</head>
<body>
<div class="page">
  <div class="scene" role="img" aria-label="Foto: dunkler Café- und Pausenraum mit Holztischen und Stühlen"></div>
  <div class="machines" role="img" aria-label="Foto: beleuchtete Getränke- und Snackautomaten"></div>

  <header>
    <div class="abs logo">K&amp;L Vendora</div>
    <nav class="nav">
      <a class="abs" style="left:191px" href="#">HOME</a>
      <a class="abs" style="left:274px" href="#">ÜBER UNS</a>
      <a class="abs active" href="#">PRODUKTE
        <svg width="9" height="6" viewBox="0 0 9 6"><path d="M1 1l3.5 3.5L8 1" fill="none" stroke="currentColor" stroke-width="1.4"/></svg></a>
      <a class="abs" style="left:492px;top:36px" href="#">KONTAKT</a>
      <a class="abs meta" style="left:602px" href="#">kl.vendora@mail-beispiel.de</a>
      <a class="abs meta" style="left:769px" href="#">0371-558214</a>
    </nav>
    <div class="abs rule" style="top:68px"></div>
    <ul class="abs dropdown">
      <li>InCup-Systeme</li><li>Standgeräte</li><li class="current">Kaltgetränkeautomaten</li><li>Snackautomaten</li><li>Wasserspender</li>
    </ul>
  </header>

  <section class="hero">
    <h1 class="abs headline">AUTOMATEN<br>FÜR <em>BÜRO</em><br>UND <em>BETRIEB</em></h1>
    <p class="abs subline">Getränke, Snacks und Wasser –<br>zuverlässig, praktisch und direkt vor Ort.</p>
    <div class="abs btn btn-primary">KONTAKT AUFNEHMEN</div>
    <div class="abs btn btn-outline">PRODUKTE</div>

    <div class="abs features"></div>
    <div class="abs feature" style="left:97px">
      <svg width="28" height="28" viewBox="0 0 28 28" fill="none" stroke="#fff" stroke-width="1.4"><circle cx="9" cy="11" r="4"/><path d="M2 25c0-5 3-7 7-7s7 2 7 7"/><circle cx="20" cy="8" r="5"/><path d="M18 8l1.5 1.5L22.5 6"/></svg>
      <span>Individuelle<br>Beratung<br>vor Ort</span></div>
    <div class="abs feature" style="left:284px">
      <svg width="28" height="28" viewBox="0 0 28 28" fill="none" stroke="#fff" stroke-width="1.4"><path d="M5 16v-3a9 9 0 0118 0v3"/><rect x="3" y="15" width="5" height="7" rx="2"/><rect x="20" y="15" width="5" height="7" rx="2"/><circle cx="14" cy="14" r="4"/></svg>
      <span>Zuverlässiger<br>Kundenservice<br>in Sachsen</span></div>
    <div class="abs feature" style="left:472px">
      <svg width="28" height="28" viewBox="0 0 28 28" fill="none" stroke="#fff" stroke-width="1.4"><rect x="5" y="3" width="18" height="22" rx="1"/><path d="M8 7h9M8 11h9M8 15h9M20 7v8M9 20h7"/></svg>
      <span>Moderne,<br>leistungsstarke<br>Geräte</span></div>
    <div class="abs feature" style="left:659px">
      <svg width="28" height="28" viewBox="0 0 28 28" fill="none" stroke="#fff" stroke-width="1.4"><circle cx="11" cy="11" r="4"/><path d="M11 3v3M11 16v3M3 11h3M16 11h3M5.5 5.5l2 2M14.5 14.5l2 2M16.5 5.5l-2 2M5.5 16.5l2-2"/><circle cx="20" cy="20" r="3"/><path d="M20 14v2M20 24v2M14 20h2M24 20h2"/></svg>
      <span>Flexible und<br>wirtschaftliche<br>Konzepte</span></div>
  </section>

  <section class="about">
    <h2 class="abs section-title" style="top:593px">ÜBER UNS</h2>
    <div class="abs timeline"></div>
    <div class="abs dot" style="top:681px"></div>
    <div class="abs dot" style="top:789px"></div>
    <div class="abs dot" style="top:898px"></div>
    <div class="abs dot" style="top:1006px"></div>

    <div class="abs" style="left:524px;top:634px;width:58px;height:58px;border-radius:50%;background:var(--red-deep)"></div>
    <div class="abs photo-round" style="left:477px;top:640px;background:radial-gradient(circle at 40% 40%,#e8e6e2,#9c9894)" role="img" aria-label="Foto: heller Büroarbeitsplatz"></div>
    <div class="abs photo-round" style="left:323px;top:753px;background:radial-gradient(circle at 50% 40%,#dcd8d2,#8a857e)" role="img" aria-label="Foto: Kaffeetasse und Snack am Schreibtisch"></div>
    <div class="abs photo-round" style="left:477px;top:861px;background:radial-gradient(circle at 40% 40%,#ece9e4,#a6a09a)" role="img" aria-label="Foto: Wasserspender im Büro"></div>
    <div class="abs photo-round" style="left:323px;top:970px;background:radial-gradient(circle at 50% 50%,#c7cbd0,#6c727a)" role="img" aria-label="Foto: Person im Pausenbereich"></div>

    <div class="abs step left" style="top:683px"><h3>1. REGIONALER PARTNER</h3><p>K&amp;L VENDORA IST IHR PARTNER FÜR MODERNE<br>AUTOMATENLÖSUNGEN IN CHEMNITZ UND SACHSEN.</p></div>
    <div class="abs step right" style="top:791px"><h3>2. LÖSUNGEN FÜR DEN ALLTAG</h3><p>WIR BIETEN GETRÄNKE, SNACKS, WASSER UND INCUP-<br>SYSTEME FÜR BÜROS, BETRIEBE UND AUFENTHALTSBEREICHE.</p></div>
    <div class="abs step left" style="top:900px"><h3>3. INDIVIDUELL GEPLANT</h3><p>JEDES KONZEPT WIRD PASSEND ZUM STANDORT,<br>BEDARF UND DEN MENSCHEN VOR ORT ABGESTIMMT.</p></div>
    <div class="abs step right" style="top:1008px"><h3>4. ALLES AUS EINER HAND</h3><p>VON DER BERATUNG ÜBER DIE AUFSTELLUNG BIS ZUR REGELMÄSSIGEN<br>BEFÜLLUNG BEGLEITEN WIR DEN GESAMTEN ABLAUF.</p></div>
  </section>

  <section class="products">
    <div class="abs card" style="left:62px;top:1154px;background:linear-gradient(90deg,#3a3a3c,#222224 45%,#4a3a2c 70%,#1d1a18)" role="img" aria-label="Foto: Snackautomat">
      <div class="cap"><h4>SNACKAUTOMATEN</h4><p>Snacks für Pausen<br>und zwischendurch.</p></div></div>
    <div class="abs card" style="left:604px;top:1154px;background:linear-gradient(120deg,#1c1c1e 30%,#cfd0d2 45%,#e6e6e6 70%,#b9b9bb)" role="img" aria-label="Foto: Wasserspender">
      <div class="cap"><h4>WASSERSPENDER</h4><p>Frisches Trinkwasser<br>direkt vor Ort.</p></div></div>
    <h2 class="abs section-title" style="top:1156px">UNSERE PRODUKTE</h2>
    <div class="abs card" style="left:198px;top:1234px;background:linear-gradient(90deg,#d4d1cc,#bdb8b2 50%,#3c5d8a 65%,#b7b2ab)" role="img" aria-label="Foto: Standgerät für Heißgetränke">
      <div class="cap"><h4>STANDGERÄTE</h4><p>Flexible Automatenlösungen für<br>Büro und Betrieb.</p></div></div>
    <div class="abs card" style="left:468px;top:1234px;background:linear-gradient(180deg,#2a3a55,#4a5d70 35%,#3b3b3d 60%,#1f1f21)" role="img" aria-label="Foto: Kaltgetränkeautomat">
      <div class="cap"><h4>KALTGETRÄNKE- AUTOMATEN</h4><p>Getränke jederzeit griffbereit.</p></div></div>
    <div class="abs card" style="left:333px;top:1346px;border-color:var(--red-deep);background:linear-gradient(160deg,#3a3a3c,#2a2a2c 45%,#1a1a1b)" role="img" aria-label="Foto: InCup-Heißgetränkeautomat mit Touchscreen">
      <div class="cap"><h4>INCUP-SYSTEME</h4><p>Heißgetränke schnell<br>und sauber zubereitet.</p></div></div>
    <div class="abs arrow" style="left:385px"><svg width="28" height="28" viewBox="0 0 28 28"><path d="M16 9l-5 5 5 5" fill="none" stroke="#111" stroke-width="2"/></svg></div>
    <div class="abs arrow" style="left:475px"><svg width="28" height="28" viewBox="0 0 28 28"><path d="M12 9l5 5-5 5" fill="none" stroke="#111" stroke-width="2"/></svg></div>
  </section>

  <section class="contact">
    <h2 class="abs section-title" style="top:1718px">KONTAKT</h2>
    <h3 class="abs contact-lead">Wir beraten Sie gern persönlich</h3>
    <p class="abs contact-text" style="top:1811px">Sie möchten Getränke, Snacks oder frisches Wasser direkt in Ihrem Unternehmen anbieten?</p>
    <p class="abs contact-text" style="top:1848px">Nehmen Sie Kontakt mit uns auf – wir entwickeln ein passendes Automatenkonzept für Ihren Standort.</p>
    <div class="abs contact-row" style="top:1906px">
      <svg width="11" height="12" viewBox="0 0 11 12" fill="none" stroke="#fff"><path d="M5.5 11S1.5 7 1.5 4.5a4 4 0 018 0C9.5 7 5.5 11 5.5 11z"/><circle cx="5.5" cy="4.5" r="1.4"/></svg>
      <span>K&amp;L Vendora GmbH<br>Lindenauer Straße 17<br>09111 Chemnitz</span></div>
    <div class="abs contact-row" style="top:1957px">
      <svg width="11" height="12" viewBox="0 0 11 12" fill="none" stroke="#fff"><path d="M2 1h2l1 3-1.5 1a6 6 0 003 3L8 7l3 1v2a1 1 0 01-1 1A9 9 0 011 2a1 1 0 011-1z"/></svg>
      <span>0371-558214</span></div>
    <div class="abs contact-row" style="top:1981px">
      <svg width="11" height="12" viewBox="0 0 11 12" fill="none" stroke="#fff"><rect x="1" y="2.5" width="9" height="7"/><path d="M1 2.5l4.5 4 4.5-4"/></svg>
      <span>kl.vendora@mail-beispiel.de</span></div>
    <div class="abs map" role="img" aria-label="Karte mit dem Firmenstandort in Chemnitz"></div>
  </section>

  <footer>
    <div class="abs rule" style="top:2085px"></div>
    <div class="abs foot-col" style="left:68px"><h5>K&amp;L Vendora GmbH</h5><p class="foot-about">Moderne Automaten- und Verpflegungslösungen für Unternehmen in Chemnitz und ganz Sachsen.</p></div>
    <div class="abs foot-col" style="left:310px"><h5>Navigation</h5>Home<br>Produkte<br>Über uns<br>Kontakt</div>
    <div class="abs foot-col" style="left:414px"><h5>Produkte</h5>InCup-Systeme<br>Standgeräte<br>Kaltgetränkeautomaten<br>Snackautomaten<br>Wasserspender</div>
    <div class="abs foot-col" style="left:557px"><h5>Rechtliches</h5>Impressum<br>Datenschutz<br>Erklärung zur Barrierefreiheit</div>
    <div class="abs foot-col" style="left:717px"><h5>Kontakt</h5>0371-558214<br>kl.vendora@mail-beispiel.de</div>
  </footer>
</div>
</body>
</html>
```